Powerpoint template and intro presentation

I have a short presentation of 6 slides that I'd like to be made pretty, see attached below - called target companies Intro.

I'd also like a template incorporating my logo which I have attached below as well

I've attached a jpeg with the logo with white background that is the logo that I would like to incorporate.

Powerpoint and logo file has been uploaded

```html
<!DOCTYPE html>
<html lang="en">
<head>
<meta charset="utf-8">
<title>Charts 2 – Northfield Data Services</title>
<link href="https://fonts.googleapis.com/css2?family=Questrial&display=swap" rel="stylesheet">
<style>
  :root {
    --backdrop: #ece8e1;
    --slide: #ffffff;
    --green: #7ab929;
    --green-dark: #4f7d18;
    --green-light: #b4d884;
    --green-band: #c9e3aa;
    --charcoal: #47494d;
    --charcoal-dark: #2f3134;
    --grey: #8c8e92;
    --rule: #cfd1d3;
    --panel: #dfe3e6;
    --ink: #55585c;
    --axis: #b9bbbd;
  }
  html, body {
    margin: 0;
    width: 1200px;
    height: 1000px;
    overflow: hidden;
    background: var(--backdrop);
    font-family: "Questrial", "Century Gothic", sans-serif;
  }
  .slide {
    position: absolute;
    left: 33px;
    top: 70px;
    width: 1137px;
    height: 852px;
    background: var(--slide);
    box-shadow: 0 2px 6px rgba(0,0,0,0.18);
  }
  .slide svg { display: block; }
  .brand-name { fill: var(--green); font-size: 21px; }
  .brand-tagline { fill: var(--green); font-size: 11px; letter-spacing: 7px; }
  .slide-title { fill: var(--green); font-size: 42px; }
  .panel-title { fill: var(--ink); font-size: 31px; }
  .legend-text { fill: var(--ink); font-size: 27px; }
  .axis-text { fill: var(--ink); font-size: 25px; }
  .page-number { fill: #ffffff; font-size: 17px; }
</style>
</head>
<body>
<div class="slide">
  <svg width="1137" height="852" viewBox="33 70 1137 852" xmlns="http://www.w3.org/2000/svg">
    <!-- Brand -->
    <g class="brand">
      <circle cx="166" cy="138" r="20" fill="var(--green)"/>
      <text class="brand-name" x="167" y="190" text-anchor="middle">NORTHFIELD</text>
      <text class="brand-tagline" x="170" y="204" text-anchor="middle">DATA SERVICES</text>
    </g>

    <!-- Title -->
    <text class="slide-title" x="262" y="175">Charts 2</text>
    <rect x="262" y="187" width="908" height="7" fill="var(--green-band)"/>
    <rect x="262" y="198" width="908" height="2" fill="var(--rule)"/>

    <!-- Panel headings -->
    <rect x="90" y="237" width="502" height="53" fill="var(--panel)"/>
    <text class="panel-title" x="341" y="275" text-anchor="middle">Pie Chart</text>
    <rect x="610" y="237" width="503" height="53" fill="var(--panel)"/>
    <text class="panel-title" x="861" y="275" text-anchor="middle">Bar Chart</text>

    <!-- Pie chart -->
    <g class="pie-chart">
      <path d="M418,522 A153,67 0 0 1 186.2,579.4 L186.2,611.4 A153,67 0 0 0 418,554 Z" fill="var(--green-dark)"/>
      <path d="M186.2,579.4 A153,67 0 0 1 112,522 L112,554 A153,67 0 0 0 186.2,611.4 Z" fill="var(--charcoal-dark)"/>
      <path d="M265,522 L265,455 A153,67 0 1 1 186.2,579.4 Z" fill="var(--green)"/>
      <path d="M265,522 L186.2,579.4 A153,67 0 0 1 124.6,495.4 Z" fill="var(--charcoal)"/>
      <path d="M265,522 L124.6,495.4 A153,67 0 0 1 187.1,464.3 Z" fill="var(--green-light)"/>
      <path d="M265,522 L187.1,464.3 A153,67 0 0 1 265,455 Z" fill="var(--grey)"/>
    </g>
    <g class="pie-legend">
      <rect x="452" y="482" width="15" height="15" fill="var(--green)"/>
      <text class="legend-text" x="474" y="500">1st Qtr</text>
      <rect x="452" y="525" width="15" height="15" fill="var(--charcoal)"/>
      <text class="legend-text" x="474" y="543">2nd Qtr</text>
      <rect x="452" y="568" width="15" height="15" fill="var(--green-light)"/>
      <text class="legend-text" x="474" y="586">3rd Qtr</text>
      <rect x="452" y="611" width="15" height="15" fill="var(--grey)"/>
      <text class="legend-text" x="474" y="629">4th Qtr</text>
    </g>

    <!-- Bar chart axes -->
    <g class="bar-axes" stroke="var(--axis)" stroke-width="1.5" fill="none">
      <line x1="815" y1="347" x2="815" y2="700"/>
      <line x1="871" y1="347" x2="871" y2="700"/>
      <line x1="927" y1="347" x2="927" y2="700"/>
      <line x1="785" y1="368" x2="815" y2="347"/>
      <line x1="785" y1="368" x2="785" y2="718"/>
      <line x1="785" y1="718" x2="815" y2="700"/>
      <line x1="841" y1="718" x2="871" y2="700"/>
      <line x1="897" y1="718" x2="927" y2="700"/>
      <line x1="776" y1="718" x2="785" y2="718"/>
      <line x1="776" y1="368" x2="785" y2="368"/>
      <line x1="776" y1="456" x2="785" y2="456"/>
      <line x1="776" y1="543" x2="785" y2="543"/>
      <line x1="776" y1="631" x2="785" y2="631"/>
    </g>

    <!-- Bars: category 4 -->
    <g class="bar">
      <polygon points="794,389 806,381 874,381 862,389" fill="var(--green-dark)"/>
      <polygon points="862,389 874,381 874,415 862,423" fill="#6f8a4c"/>
      <rect x="794" y="389" width="25" height="34" fill="var(--green)"/>
      <rect x="819" y="389" width="16" height="34" fill="var(--charcoal)"/>
      <rect x="835" y="389" width="28" height="34" fill="var(--green-light)"/>
      <polygon points="819,389 831,381 847,381 835,389" fill="var(--charcoal-dark)"/>
    </g>
    <!-- Category 3 -->
    <g class="bar">
      <polygon points="794,476 806,468 853,468 841,476" fill="var(--green-dark)"/>
      <polygon points="841,476 853,468 853,502 841,510" fill="#6f8a4c"/>
      <rect x="794" y="476" width="20" height="34" fill="var(--green)"/>
      <rect x="814" y="476" width="10" height="34" fill="var(--charcoal)"/>
      <rect x="824" y="476" width="17" height="34" fill="var(--green-light)"/>
      <polygon points="814,476 826,468 836,468 824,476" fill="var(--charcoal-dark)"/>
    </g>
    <!-- Category 2 -->
    <g class="bar">
      <polygon points="794,564 806,556 857,556 845,564" fill="var(--green-dark)"/>
      <polygon points="845,564 857,556 857,590 845,598" fill="#6f8a4c"/>
      <rect x="794" y="564" width="14" height="34" fill="var(--green)"/>
      <rect x="808" y="564" width="25" height="34" fill="var(--charcoal)"/>
      <rect x="833" y="564" width="12" height="34" fill="var(--green-light)"/>
      <polygon points="808,564 820,556 845,556 833,564" fill="var(--charcoal-dark)"/>
    </g>
    <!-- Category 1 -->
    <g class="bar">
      <polygon points="794,652 806,644 855,644 843,652" fill="var(--green-dark)"/>
      <polygon points="843,652 855,644 855,678 843,686" fill="#6f8a4c"/>
      <rect x="794" y="652" width="24" height="34" fill="var(--green)"/>
      <rect x="818" y="652" width="14" height="34" fill="var(--charcoal)"/>
      <rect x="832" y="652" width="11" height="34" fill="var(--green-light)"/>
      <polygon points="818,652 830,644 844,644 832,652" fill="var(--charcoal-dark)"/>
    </g>

    <!-- Bar chart labels -->
    <g class="axis-labels">
      <text class="axis-text" x="760" y="422" text-anchor="end">Category 4</text>
      <text class="axis-text" x="760" y="510" text-anchor="end">Category 3</text>
      <text class="axis-text" x="760" y="598" text-anchor="end">Category 2</text>
      <text class="axis-text" x="760" y="686" text-anchor="end">Category 1</text>
      <text class="axis-text" x="785" y="766" text-anchor="middle">0</text>
      <text class="axis-text" x="841" y="766" text-anchor="middle">10</text>
      <text class="axis-text" x="897" y="766" text-anchor="middle">20</text>
    </g>
    <g class="bar-legend">
      <rect x="975" y="504" width="15" height="15" fill="var(--green)"/>
      <text class="legend-text" x="997" y="522">Series 1</text>
      <rect x="975" y="547" width="15" height="15" fill="var(--charcoal)"/>
      <text class="legend-text" x="997" y="565">Series 2</text>
      <rect x="975" y="590" width="15" height="15" fill="var(--green-light)"/>
      <text class="legend-text" x="997" y="608">Series 3</text>
    </g>

    <!-- Footer -->
    <rect x="33" y="862" width="1024" height="6" fill="var(--green-band)"/>
    <rect x="33" y="873" width="1024" height="2" fill="var(--rule)"/>
    <circle cx="1090" cy="876" r="22" fill="var(--green)"/>
    <text class="page-number" x="1090" y="882" text-anchor="middle">10</text>
  </svg>
</div>
</body>
</html>
```